Technological Event Invitation

We need a invitation design for a technological event we are hosting along with our partner. The target of this event are Vice president, Managers and CEO of the most important companies (bank, insurrance companies, other) in the dominican republic.

It is a flat invitation and the size is 5” x 7”.

Title: API Management
"Transforma tu negocio con API Management a través de la estrategia de digitalización"
Date: Jueves 10 de Marzo del 2016
Time: 9:00 am - 5 pm.
Place: Resturant Casa Rivolta C/ Marcos Ibarra Lugo esq. Tomás Revel.
Host: Novaldo, SRL & KV Systems
RSVP: 809 555 47 13

The final design should have two logo one being Novaldo ( the company hosting the event) and KV logo ( partner). Please consider that the desgin should represent tecnhology world.

Target Market(s)

Financial Institutions,Corporations, Goverment Institution

Industry/Entity Type

Event

Requirements
Must have
• 1. Kv logo
• 2. novaldo Logo
• 3. The invitation should show that the is a tecnological event on APIM.
Nice to have
• our colors integrated on the invitations

```html
<!DOCTYPE html>
<html lang="es">
<head>
<meta charset="utf-8">
<title>API Management — Invitación</title>
<link href="https://fonts.googleapis.com/css2?family=Bebas+Neue&family=Oswald:wght@400;500;700&display=swap" rel="stylesheet">
<style>
  :root {
    --bg-deep: #0b0b0c;
    --bg-mid: #232426;
    --ink: #ffffff;
    --ink-soft: #d9d9d9;
    --teal: #3fd0c5;
    --teal-dark: #1f8f88;
    --teal-shade: #167069;
    --band-ink: #0f1a1a;
    --brand-red: #e2392c;
    --brand-blue: #1aa0dc;
  }
  * { margin: 0; padding: 0; box-sizing: border-box; }
  html, body { width: 857px; height: 1200px; overflow: hidden; background: var(--bg-deep); }
  .invitation {
    position: relative;
    width: 857px;
    height: 1200px;
    overflow: hidden;
    background: radial-gradient(ellipse at 50% 40%, var(--bg-mid) 0%, #151516 55%, var(--bg-deep) 100%);
    color: var(--ink);
    font-family: "Oswald", "Arial Narrow", sans-serif;
  }
  .display { font-family: "Bebas Neue", "Oswald", sans-serif; font-weight: 400; }

  .hosts {
    position: absolute; top: 118px; left: 0; width: 100%;
    display: flex; justify-content: center; align-items: center; gap: 70px;
  }
  .host-primary { display: flex; align-items: center; gap: 14px; }
  .host-mark { width: 58px; height: 58px; border-radius: 50%; background: var(--brand-red); }
  .host-name { font-family: "Oswald", sans-serif; font-weight: 700; font-size: 46px; line-height: 1; color: var(--ink); letter-spacing: 1px; }
  .host-tagline { font-size: 13px; font-weight: 500; letter-spacing: 1.5px; color: var(--ink-soft); margin-top: 4px; }
  .partner { display: flex; align-items: center; gap: 12px; }
  .partner-mark { width: 50px; height: 50px; background: var(--brand-blue); }
  .partner-name { font-family: "Oswald", sans-serif; font-weight: 700; font-size: 54px; line-height: 1; color: var(--ink); }

  .presents {
    position: absolute; top: 232px; width: 100%; text-align: center;
    font-size: 22px; letter-spacing: 14px; font-weight: 400; padding-left: 14px;
  }
  .title {
    position: absolute; top: 262px; width: 100%; text-align: center; line-height: 0.86;
  }
  .title-api { display: block; font-size: 132px; letter-spacing: 4px; }
  .title-main { display: block; font-size: 142px; letter-spacing: 3px; }
  .subtitle {
    position: absolute; top: 508px; width: 100%; text-align: center;
    font-size: 19px; font-weight: 400; letter-spacing: 1.8px; line-height: 1.35; text-transform: uppercase;
  }

  .date {
    position: absolute; top: 578px; left: 395px;
    display: flex; align-items: flex-start; gap: 10px;
  }
  .date-day { font-size: 150px; line-height: 0.8; }
  .date-side { display: flex; flex-direction: column; line-height: 0.85; padding-top: 4px; }
  .date-month { font-size: 66px; }
  .date-year { font-size: 56px; }

  .venue-band { position: absolute; top: 700px; left: 130px; width: 610px; height: 150px; }
  .venue-text {
    position: absolute; top: 738px; left: 175px; width: 560px;
    transform: rotate(-3deg); transform-origin: left center;
    color: var(--band-ink); text-align: center;
  }
  .venue-name { font-size: 60px; line-height: 0.95; }
  .venue-address { font-size: 30px; line-height: 1; letter-spacing: 0.5px; }

  .rsvp {
    position: absolute; top: 930px; left: 150px;
    display: flex; align-items: center; gap: 14px;
  }
  .rsvp-label {
    writing-mode: vertical-rl; transform: rotate(180deg);
    font-size: 18px; letter-spacing: 5px; font-weight: 500;
  }
  .rsvp-phone { font-size: 116px; line-height: 1; letter-spacing: 2px; }
</style>
</head>
<body>
<main class="invitation">
  <header class="hosts">
    <div class="host-primary">
      <span class="host-mark"></span>
      <div>
        <div class="host-name">NOVALDO</div>
        <div class="host-tagline">IT CONSULTING AND SERVICES</div>
      </div>
    </div>
    <div class="partner">
      <span class="partner-mark"></span>
      <span class="partner-name">KV</span>
    </div>
  </header>

  <p class="presents">PRESENTAS</p>

  <h1 class="title display">
    <span class="title-api">API</span>
    <span class="title-main">MANAGEMENT</span>
  </h1>

  <p class="subtitle">Transforma tu negocio con API Management a<br>través de la estrategia de digitalización</p>

  <div class="date display">
    <span class="date-day">10</span>
    <span class="date-side">
      <span class="date-month">MAR</span>
      <span class="date-year">2016</span>
    </span>
  </div>

  <svg class="venue-band" viewBox="0 0 610 150" aria-hidden="true">
    <polygon points="0,70 45,66 45,134 0,140 18,104" fill="var(--teal-dark)"/>
    <polygon points="565,20 610,16 592,50 610,84 565,88" fill="var(--teal-dark)"/>
    <polygon points="45,66 70,78 70,134 45,134" fill="var(--teal-shade)"/>
    <polygon points="565,20 540,36 540,88 565,88" fill="var(--teal-shade)"/>
    <polygon points="40,44 570,16 570,100 40,128" fill="var(--teal)"/>
  </svg>
  <div class="venue-text display">
    <div class="venue-name">RESTURANT CASA RIVOLTA</div>
    <div class="venue-address">C/ MARCOS IBARRA LUGO ESQ. TOMÁS REVEL</div>
  </div>

  <div class="rsvp">
    <span class="rsvp-label">RSVP</span>
    <span class="rsvp-phone display">809 555 47 13</span>
  </div>
</main>
</body>
</html>
```